Finance Product Agency Business Card Design

We're an agency that provides products (service contracts, gap insurance, tire and wheel, etc) and support to dealership finance departments. We specialize in training finance producers to maximize their potential and also keep them up to date on the ever changing compliance and legal landscape. I'll attach an image of our logo, excited to see what you all come up with. Would also be interested in discussing our new website design with the winner.

Target Market(s)

auto dealerships

Industry/Entity Type

Business

Contact Information for Business Card

Mark Dolvery
Phone 317.624.5583
Fax 855.472.3308
email Mark.Dolvery@brightlanecoverage.example

Requirements
Must have
• basic contact information
Nice to have
• looking for something professional but modern

```html
<!DOCTYPE html>
<html lang="en">
<head>
<meta charset="utf-8">
<title>Brightlane Coverage – Business Card</title>
<link href="https://fonts.googleapis.com/css2?family=Oswald:wght@500&family=Questrial&display=swap" rel="stylesheet">
<style>
  :root {
    --page-bg: #e6e4e0;
    --card-white: #ffffff;
    --navy-deep: #05090c;
    --navy-mid: #142630;
    --slate: #2f5566;
    --slate-light: #4d7385;
    --ink-light: #e6ecef;
    --ink-muted: #b9c7ce;
    --brand-ink: #2a4654;
  }
  * { box-sizing: border-box; margin: 0; padding: 0; }
  html, body { width: 1200px; height: 800px; overflow: hidden; }
  body {
    background: var(--page-bg);
    font-family: "Questrial", "Century Gothic", sans-serif;
    position: relative;
  }
  .card {
    position: absolute;
    left: 320px;
    width: 560px;
    height: 320px;
    border-radius: 14px;
    overflow: hidden;
    box-shadow: 0 6px 18px rgba(0,0,0,0.18);
  }
  /* Front */
  .card-front { top: 50px; background: var(--card-white); }
  .card-front .wave { position: absolute; left: 0; top: 0; width: 560px; height: 320px; }
  .front-brand {
    position: absolute; left: 40px; top: 78px;
    display: flex; align-items: center; gap: 12px;
  }
  .brand-dot {
    width: 38px; height: 38px; border-radius: 50%;
    background: var(--brand-ink);
  }
  .brand-name {
    font-family: "Oswald", "Arial Narrow", sans-serif;
    font-weight: 500;
    font-size: 34px;
    letter-spacing: 0.5px;
    color: var(--brand-ink);
    text-transform: uppercase;
    line-height: 1;
  }
  .contact-list {
    position: absolute; left: 36px; top: 222px;
    list-style: none;
    color: var(--ink-light);
    font-size: 13.5px;
    line-height: 19px;
  }
  .contact-list li { display: flex; align-items: center; gap: 10px; }
  .contact-list svg { width: 13px; height: 13px; flex: none; }
  .holder {
    position: absolute; right: 36px; top: 226px;
    text-align: right;
  }
  .holder-name {
    font-family: "Oswald", "Arial Narrow", sans-serif;
    font-weight: 500;
    font-size: 19px;
    letter-spacing: 1px;
    color: var(--slate-light);
    text-transform: uppercase;
  }
  .holder-title { font-size: 15px; color: var(--ink-light); margin-top: 2px; }

  /* Back */
  .card-back {
    top: 430px;
    background: linear-gradient(180deg, var(--navy-deep) 0%, var(--navy-mid) 55%, var(--slate) 100%);
  }
  .back-brand {
    position: absolute; left: 0; right: 0; top: 118px;
    display: flex; justify-content: center; align-items: center; gap: 14px;
  }
  .back-brand .brand-dot { background: var(--slate-light); width: 44px; height: 44px; }
  .back-brand .brand-name { color: var(--ink-light); font-size: 42px; }
  .back-web {
    position: absolute; left: 0; right: 0; top: 258px;
    text-align: center;
    color: var(--ink-light);
    font-size: 14px;
    letter-spacing: 0.3px;
  }
</style>
</head>
<body>

<section class="card card-front" aria-label="Business card front">
  <svg class="wave" viewBox="0 0 560 320" aria-hidden="true">
    <defs>
      <linearGradient id="frontDark" x1="0" y1="0" x2="0" y2="1">
        <stop offset="0" stop-color="#05090c"/>
        <stop offset="1" stop-color="#1c3440"/>
      </linearGradient>
    </defs>
    <path d="M0 196 C160 196 300 160 560 168 L560 320 L0 320 Z" fill="#4d7385"/>
    <path d="M0 206 C160 206 310 176 560 184 L560 320 L0 320 Z" fill="#ffffff"/>
    <path d="M0 210 C160 210 310 182 560 190 L560 320 L0 320 Z" fill="url(#frontDark)"/>
  </svg>

  <div class="front-brand">
    <span class="brand-dot"></span>
    <span class="brand-name">Brightlane Coverage</span>
  </div>

  <ul class="contact-list">
    <li>
      <svg viewBox="0 0 16 16"><rect width="16" height="16" rx="3" fill="#2f5566"/><path d="M5 3.5l2 2-1 1.2c.6 1.3 1.6 2.3 2.9 2.9l1.2-1 2 2-1.2 1.4C7.6 11.7 4.3 8.4 3.9 5.1z" fill="#e6ecef"/></svg>
      <span>317.624.5583</span>
    </li>
    <li>
      <svg viewBox="0 0 16 16"><rect width="16" height="16" rx="3" fill="#2f5566"/><rect x="4" y="3" width="8" height="4" fill="#e6ecef"/><rect x="3" y="7" width="10" height="5" rx="1" fill="#e6ecef"/><rect x="5" y="9" width="6" height="1.5" fill="#2f5566"/></svg>
      <span>855.472.3308</span>
    </li>
    <li>
      <svg viewBox="0 0 16 16"><rect width="16" height="16" rx="3" fill="#2f5566"/><rect x="3" y="4.5" width="10" height="7" fill="#e6ecef"/><path d="M3 4.5l5 4 5-4" fill="none" stroke="#2f5566" stroke-width="1.2"/></svg>
      <span>Mark.Dolvery@brightlanecoverage.example</span>
    </li>
    <li>
      <svg viewBox="0 0 16 16"><rect width="16" height="16" rx="3" fill="#2f5566"/><circle cx="8" cy="8" r="4.5" fill="none" stroke="#e6ecef" stroke-width="1.1"/><path d="M3.5 8h9M8 3.5c-2 2.5-2 6.5 0 9M8 3.5c2 2.5 2 6.5 0 9" fill="none" stroke="#e6ecef" stroke-width="1"/></svg>
      <span>www.brightlanecoverage.example</span>
    </li>
  </ul>

  <div class="holder">
    <div class="holder-name">Mark Dolvery</div>
    <div class="holder-title">General Manager</div>
  </div>
</section>

<section class="card card-back" aria-label="Business card back">
  <div class="back-brand">
    <span class="brand-dot"></span>
    <span class="brand-name">Brightlane Coverage</span>
  </div>
  <div class="back-web">www.brightlanecoverage.example</div>
</section>

</body>
</html>
```